Law Firm Needs a Stationery Design

We need a stationery design for a law firm based in the East African region called 'Mbweteka Olinyo & Company Advocates'. We are a law firm specializing in commercial, public and constitutional law. Our practice areas include Telecommunications Law, Mining Law, Oil and Energy Law, Real Estate and Land Development Law, Employment Law, Family Law, Civil and Criminal Litigation, Constitutional Law, Company Secretariat and more. We represent a wide variety of clients, ranging from individuals to corporations and approach each case with full attention, dedication and legal acumen in order to protect the interests of our clients. The final stationary design should communicate innovation and expertise to meet our clients’ legal needs.
Target Market(s)
New clients, current and former clients, other lawyers in and outside of our practice area, or other professionals, contacts and centers of influence within the region
Industry/Entity Type
Real Estate
Colors
Designer to choose colors to be used in the design.
Look and feel
Each slider illustrates characteristics of the customer's brand and the style your logo design should communicate.

```html
<!DOCTYPE html>
<html lang="en">
<head>
<meta charset="utf-8">
<title>Mbweteka Olinyo &amp; Company Advocates — Stationery</title>
<link rel="stylesheet" href="https://fonts.googleapis.com/css2?family=Tinos&family=Open+Sans:wght@400&display=swap">
<style>
  :root {
    --page: #ffffff;
    --paper: #fdfdfd;
    --edge: #b9b9b9;
    --green: #5ba67a;
    --green-deep: #4c9468;
    --tan: #a89478;
    --ink: #333333;
    --muted: #777777;
    --caption: #6b6b6b;
  }
  * { box-sizing: border-box; margin: 0; padding: 0; }
  html, body { width: 1200px; height: 770px; overflow: hidden; background: var(--page); }
  .board { position: relative; width: 1200px; height: 770px; }

  .label { position: absolute; font: 8.5px "Open Sans", sans-serif; color: var(--ink); white-space: nowrap; }

  .sheet { position: absolute; background: var(--paper); border: 1px solid var(--edge); }

  .lockup { position: absolute; left: 0; right: 0; text-align: center; font-family: "Tinos", serif; color: var(--tan); line-height: 1.05; }
  .lockup .mark { display: block; margin: 0 auto; border-radius: 50%; background: var(--green); }
  .lockup .firm { display: block; }
  .lockup .tag { display: block; }

  .contact { position: absolute; left: 0; right: 0; text-align: center; font: 6.2px "Open Sans", sans-serif; color: var(--muted); white-space: nowrap; }

  /* Letterhead */
  .letterhead { left: 101px; top: 84px; width: 425px; height: 601px; }
  .letterhead .lockup { top: 496px; }
  .letterhead .mark { width: 34px; height: 34px; margin-bottom: 10px; }
  .letterhead .firm { font-size: 21px; }
  .letterhead .tag { font-size: 12.5px; }
  .letterhead .contact { top: 584px; }

  /* Business cards */
  .card-front { left: 36px; top: 182px; width: 183px; height: 104px; }
  .card-front .lockup { top: 26px; }
  .card-front .mark { width: 22px; height: 22px; margin-bottom: 8px; }
  .card-front .firm { font-size: 15px; }
  .card-front .tag { font-size: 8.5px; }

  .card-back { left: 239px; top: 182px; width: 181px; height: 104px; background: var(--green); color: #fff; }
  .card-back .person { position: absolute; top: 41px; left: 0; right: 0; text-align: center; font: 9px/1.1 "Tinos", serif; }
  .card-back .contact { color: #eef6f0; font-size: 5.4px; line-height: 1.65; top: 82px; }

  /* Complimentary slip */
  .slip { left: 549px; top: 85px; width: 308px; height: 188px; z-index: 3; }
  .slip .lockup { top: 124px; }
  .slip .mark { width: 22px; height: 22px; margin-bottom: 8px; }
  .slip .firm { font-size: 15px; }
  .slip .tag { font-size: 8.5px; }

  /* Envelope front */
  .envelope-front { left: 164px; top: 313px; width: 489px; height: 232px; z-index: 2; }
  .envelope-front .lockup { top: 154px; }
  .envelope-front .mark { width: 26px; height: 26px; margin-bottom: 8px; }
  .envelope-front .firm { font-size: 16px; }
  .envelope-front .tag { font-size: 9.5px; }
  .envelope-front .contact { top: 216px; }

  /* Envelope open */
  .envelope-open { position: absolute; left: 675px; top: 235px; width: 489px; height: 310px; }
  .envelope-open svg { display: block; }

  .caption { position: absolute; left: 616px; top: 731px; font: 15px "Open Sans", sans-serif; color: var(--caption); white-space: nowrap; }
</style>
</head>
<body>
<main class="board">
  <span class="label" style="left:102px;top:71px;">Letterhead</span>
  <section class="sheet letterhead">
    <div class="lockup">
      <span class="mark"></span>
      <span class="firm">Mbweteka Olinyo</span>
      <span class="tag">&amp; Company Advocates</span>
    </div>
    <p class="contact">Address Line, Lorem ipsum dolor sit amet, consectetuer adipiscing. T: 12345 12345 E: info@mboca.com W: www.mboca.com</p>
  </section>

  <span class="label" style="left:38px;top:169px;">Business Card (front/back)</span>
  <section class="sheet card-front">
    <div class="lockup">
      <span class="mark"></span>
      <span class="firm">Mbweteka Olinyo</span>
      <span class="tag">&amp; Company Advocates</span>
    </div>
  </section>
  <section class="sheet card-back">
    <p class="person">Mbweteka Olinyo<br>Principle Lawyer</p>
    <p class="contact">Address Line, Lorem ipsum dolor sit amet, consectetuer adipiscing<br>T: 12345 12345 E: info@mboca.com W: www.mboca.com</p>
  </section>

  <span class="label" style="left:551px;top:71px;">Complimentary Slip</span>
  <section class="sheet slip">
    <div class="lockup">
      <span class="mark"></span>
      <span class="firm">Mbweteka Olinyo</span>
      <span class="tag">&amp; Company Advocates</span>
    </div>
  </section>

  <section class="sheet envelope-front">
    <div class="lockup">
      <span class="mark"></span>
      <span class="firm">Mbweteka Olinyo</span>
      <span class="tag">&amp; Company Advocates</span>
    </div>
    <p class="contact">Address Line, Lorem ipsum dolor sit amet, consectetuer adipiscing. T: 12345 12345 E: info@mboca.com W: www.mboca.com</p>
  </section>

  <section class="envelope-open">
    <svg width="489" height="310" viewBox="0 0 489 310">
      <defs>
        <linearGradient id="pocket-shade" x1="0" y1="0" x2="0" y2="1">
          <stop offset="0" stop-color="#4a8f65"/>
          <stop offset="1" stop-color="#5ba67a"/>
        </linearGradient>
      </defs>
      <rect x="0.5" y="0.5" width="488" height="309" fill="#fdfdfd" stroke="#d4d4d4"/>
      <path d="M0 0 H459 Q488 0 488 30 V78 H0 Z" fill="var(--green)"/>
      <path d="M22 78 H466 L447 135 Q443 150 425 150 H55 Q40 150 36 135 Z" fill="url(#pocket-shade)"/>
      <circle cx="243" cy="40" r="13" fill="#ffffff"/>
    </svg>
  </section>
  <span class="label" style="left:1078px;top:554px;">Envelope (front/open)</span>

  <p class="caption">Concept: In the symbol MO depicts brand name as well as showing scale of justice</p>
</main>
</body>
</html>
```